Neighbor of existing customer door hanger

We are a landscaping services company (Pest Control & Lawn Fertilization). I am looking for a piece that my sales people can leave behind at the neighbors of our current customers offering our services to them.

I'm not a graphics guy, not even close, I started making a sample that is not any good, but it might give the general idea. I have attached that design here. There is a template available from the printer for 4.25 x 11". I have included that as well

Target Market(s)

Women homeowners 35-50

Industry/Entity Type

Landscape Gardening

Font styles to use
Sans Serif

Colors

Designer to choose colors to be used in the design.

Requirements
Must have
• we are looking for a space to write the name or address of our customer, include 2 specials ( 1 for pest control, 1 for Lawn fertilization and weed control) that make the neighbors feel like they are getting a deal because they are neighbors of our customer.
• the back side of the postcard will list our range of services and have a space for the salesman to write his name.
• This will be printed on a glossy cardstock (unless the designer suggests something else).
• Phone numbers, Website, logos

```html
<!DOCTYPE html>
<html lang="en">
<head>
<meta charset="utf-8">
<title>Fairlawn Door Hangers</title>
<link href="https://fonts.googleapis.com/css2?family=Oswald:wght@400;500&family=Open+Sans:wght@400;600;700&family=Kaushan+Script&display=swap" rel="stylesheet">
<style>
  :root {
    --canvas: #e4e2df;
    --green-deep: #16692a;
    --green-dark: #2b8a34;
    --green: #4fa535;
    --green-soft: #7cbf45;
    --green-pale: #cfe7a6;
    --lime: #9ccf3d;
    --yellow: #fff200;
    --white: #ffffff;
    --ink: #2b2b2b;
  }
  * { margin: 0; padding: 0; box-sizing: border-box; }
  html, body { width: 1016px; height: 1200px; overflow: hidden; background: var(--canvas); }
  body { position: relative; font-family: "Open Sans", sans-serif; }

  .hanger {
    position: absolute; top: 56px; width: 420px; height: 1088px;
    background: var(--white); overflow: hidden;
    box-shadow: 0 3px 10px rgba(0,0,0,.25);
  }
  .hanger--front { left: 60px; }
  .hanger--back { left: 536px; }

  .hanger__photo { position: absolute; left: 0; top: 0; width: 420px; height: 530px; }
  .hanger--front .hanger__photo { background: linear-gradient(180deg, #b9c7d6 0%, #cfc6b8 36%, #8f8c83 55%, #5e9a3a 70%, #4b8a2e 100%); }
  .hanger--back .hanger__photo { background: linear-gradient(180deg, #5d7a4a 0%, #8a8a6a 27%, #a79c86 40%, #6fa83c 56%, #4d9a2f 100%); }

  .hanger__hole {
    position: absolute; left: 152px; top: 38px; width: 116px; height: 116px;
    border-radius: 50%; background: var(--canvas);
  }
  .hanger__waves { position: absolute; inset: 0; width: 420px; height: 1088px; }

  .brand {
    position: absolute; left: 0; right: 0; top: 448px; text-align: center;
    font-family: "Open Sans", sans-serif; font-weight: 700; font-size: 30px;
    letter-spacing: 2px; color: var(--green-dark); line-height: 1;
  }
  .brand__rule { position: absolute; left: 118px; width: 184px; top: 490px; height: 2px; background: var(--green-dark); }

  .service-icons { position: absolute; top: 502px; left: 0; right: 0; display: flex; justify-content: center; gap: 14px; }
  .service-icons__tile { width: 44px; height: 44px; border-radius: 4px; border: 2px solid var(--white); }
  .tile--grass { background: linear-gradient(180deg, #d9eed0, #2f8f2f); }
  .tile--pest { background: linear-gradient(180deg, #f1f6e8, #a9cf7c); }
  .tile--soil { background: linear-gradient(180deg, #b7c2d8, #6b4a2a); }

  .greeting {
    position: absolute; left: 0; right: 0; top: 558px; text-align: center;
    font-family: "Kaushan Script", cursive; font-size: 26px; color: var(--white);
  }
  .headline {
    position: absolute; left: 0; right: 0; text-align: center; white-space: nowrap;
    font-family: "Oswald", sans-serif; font-weight: 500; color: var(--white);
    text-transform: uppercase; line-height: 1;
  }
  .hanger--front .headline { top: 594px; font-size: 33px; }
  .hanger--back .headline { top: 578px; font-size: 26px; letter-spacing: -0.3px; }

  .write-in {
    position: absolute; left: 16px; right: 16px; height: 44px;
    background: var(--white); border-radius: 22px;
    box-shadow: 0 2px 3px rgba(0,0,0,.25);
  }
  .hanger--front .write-in { top: 640px; }
  .hanger--back .write-in { top: 625px; left: 14px; right: 18px; }

  .write-in__label { position: absolute; left: 0; right: 0; top: 676px; text-align: center; color: var(--white); font-size: 16px; }

  .pitch { position: absolute; left: 0; right: 0; top: 690px; text-align: center; color: var(--white); }
  .pitch__lead { font-size: 16px; line-height: 22px; }
  .pitch__strong { font-size: 18px; font-weight: 700; line-height: 24px; text-transform: uppercase; }

  .service-list { position: absolute; list-style: none; }
  .service-list li { display: flex; align-items: center; gap: 10px; height: 31.5px; color: var(--white); white-space: nowrap; }
  .service-list__icon { width: 26px; height: 26px; border: 2px solid var(--white); border-radius: 3px; flex: none; display: flex; align-items: center; justify-content: center; }
  .service-list__icon::after { content: ""; width: 10px; height: 10px; border-radius: 50%; background: var(--white); }
  .hanger--front .service-list { left: 16px; top: 752px; font-size: 14px; }
  .hanger--front .service-list li { text-transform: uppercase; }
  .hanger--back .service-list { top: 712px; font-family: "Oswald", sans-serif; font-size: 14px; text-transform: uppercase; }
  .service-list--a { left: 8px; }
  .service-list--b { left: 256px; }
  .hanger--back .service-list__icon { width: 24px; height: 24px; }

  .badge { position: absolute; width: 166px; height: 166px; }
  .hanger--front .badge { left: 250px; top: 748px; }
  .hanger--back .badge { left: 258px; top: 280px; }
  .badge svg { position: absolute; inset: 0; }
  .badge__text { position: absolute; inset: 0; display: flex; flex-direction: column; align-items: center; justify-content: center; text-align: center; color: var(--green-deep); }
  .badge__eyebrow { font-size: 11px; }
  .badge__price { font-family: "Oswald", sans-serif; font-weight: 500; font-size: 40px; line-height: 1.05; }
  .badge__offer { font-family: "Oswald", sans-serif; font-size: 14px; line-height: 18px; text-transform: uppercase; }
  .hanger--front .badge__offer { font-size: 12px; letter-spacing: -0.2px; white-space: nowrap; }
  .badge__note { font-size: 12px; margin-top: 2px; }

  .tagline {
    position: absolute; left: 0; right: 0; top: 980px; text-align: center;
    font-family: "Oswald", sans-serif; font-size: 16px; color: var(--green-soft); text-transform: uppercase;
  }
  .cta {
    position: absolute; left: 18px; right: 16px; top: 1010px; height: 34px;
    background: var(--green-dark); border-radius: 17px;
    display: flex; align-items: center; justify-content: center; gap: 10px;
    color: var(--white); font-size: 21px; box-shadow: 0 2px 3px rgba(0,0,0,.25);
  }
  .cta__phone { font-weight: 700; display: flex; align-items: center; gap: 6px; }
  .cta__phone svg { width: 22px; height: 22px; }
  .website { position: absolute; left: 0; right: 0; top: 1048px; text-align: center; font-size: 22px; font-weight: 700; color: var(--ink); }
</style>
</head>
<body>

<section class="hanger hanger--front">
  <div class="hanger__photo" role="img" aria-label="Photo of a large suburban house at dusk with a hand holding a magnifying glass over a spider"></div>
  <div class="hanger__hole"></div>
  <svg class="hanger__waves" viewBox="0 0 420 1088" preserveAspectRatio="none" aria-hidden="true">
    <defs>
      <linearGradient id="frontBody" x1="0" y1="0" x2="0" y2="1">
        <stop offset="0" stop-color="#e4f2c6"/>
        <stop offset=".22" stop-color="#8cc652"/>
        <stop offset=".6" stop-color="#4fa535"/>
        <stop offset="1" stop-color="#3f962f"/>
      </linearGradient>
    </defs>
    <path d="M0,470 C70,430 170,412 420,404 L420,1088 L0,1088 Z" fill="var(--green-deep)"/>
    <path d="M0,486 C80,440 200,424 420,418 L420,1088 L0,1088 Z" fill="url(#frontBody)"/>
    <path d="M0,1000 C70,950 190,915 420,900 L420,1088 L0,1088 Z" fill="var(--lime)"/>
    <path d="M0,1030 C90,965 220,930 420,924 L420,1088 L0,1088 Z" fill="var(--white)"/>
  </svg>

  <div class="brand">Fairlawn</div>
  <div class="brand__rule"></div>
  <div class="service-icons">
    <div class="service-icons__tile tile--grass" role="img" aria-label="Grass icon"></div>
    <div class="service-icons__tile tile--pest" role="img" aria-label="Insect icon"></div>
    <div class="service-icons__tile tile--soil" role="img" aria-label="Shovel in soil icon"></div>
  </div>

  <div class="greeting">Hello neighbor!</div>
  <div class="headline">We service your friends:</div>
  <div class="write-in"></div>
  <div class="pitch">
    <div class="pitch__lead">Because your friends use our services,</div>
    <div class="pitch__strong">You get neighborhood discounts!</div>
  </div>

  <ul class="service-list">
    <li><span class="service-list__icon"></span>Full service pest control</li>
    <li><span class="service-list__icon"></span>Inside &amp; out treatments</li>
    <li><span class="service-list__icon"></span>Wasps/hornets</li>
    <li><span class="service-list__icon"></span>Mice/rats</li>
    <li><span class="service-list__icon"></span>Gophers/voles</li>
  </ul>

  <div class="badge">
    <svg viewBox="0 0 100 100" aria-hidden="true">
      <circle cx="50" cy="50" r="44" fill="var(--yellow)"/>
      <circle cx="50" cy="50" r="46" fill="none" stroke="var(--yellow)" stroke-width="7" stroke-dasharray="3 3"/>
    </svg>
    <div class="badge__text">
      <span class="badge__eyebrow">Neighbor Discount</span>
      <span class="badge__price">$9.95</span>
      <span class="badge__offer">Full service pest control</span>
      <span class="badge__note">First Service</span>
    </div>
  </div>

  <div class="tagline">Locally owned lawn &amp; pest control since 1990</div>
  <div class="cta">
    <span>FREE ESTIMATE</span>
    <span class="cta__phone">
      <svg viewBox="0 0 24 24" aria-hidden="true"><circle cx="12" cy="12" r="10" fill="none" stroke="#fff" stroke-width="2"/><path d="M8.5 7 L10.5 7 L11 9.5 L9.8 10.5 C10.5 12 12 13.5 13.5 14.2 L14.5 13 L17 13.5 L17 15.5 C17 16.3 16.3 17 15.5 17 C11 16.6 7.4 13 7 8.5 C7 7.7 7.7 7 8.5 7 Z" fill="#fff"/></svg>
      801-555-0147
    </span>
  </div>
  <div class="website">www.getfairlawn.com</div>
</section>

<section class="hanger hanger--back">
  <div class="hanger__photo" role="img" aria-label="Photo of a green backyard lawn with a stone patio, outdoor furniture and a patio umbrella"></div>
  <div class="hanger__hole"></div>
  <svg class="hanger__waves" viewBox="0 0 420 1088" preserveAspectRatio="none" aria-hidden="true">
    <defs>
      <linearGradient id="backBody" x1="0" y1="0" x2="0" y2="1">
        <stop offset="0" stop-color="#e4f2c6"/>
        <stop offset=".22" stop-color="#8cc652"/>
        <stop offset=".6" stop-color="#4fa535"/>
        <stop offset="1" stop-color="#3f962f"/>
      </linearGradient>
    </defs>
    <path d="M0,496 C60,440 170,422 420,416 L420,1088 L0,1088 Z" fill="var(--green-deep)"/>
    <path d="M0,510 C80,452 200,436 420,430 L420,1088 L0,1088 Z" fill="url(#backBody)"/>
    <path d="M0,1005 C80,960 200,935 420,912 L420,1088 L0,1088 Z" fill="var(--lime)"/>
    <path d="M0,1032 C90,972 220,945 420,934 L420,1088 L0,1088 Z" fill="var(--white)"/>
  </svg>

  <div class="badge">
    <svg viewBox="0 0 100 100" aria-hidden="true">
      <circle cx="50" cy="50" r="44" fill="var(--yellow)"/>
      <circle cx="50" cy="50" r="46" fill="none" stroke="var(--yellow)" stroke-width="7" stroke-dasharray="3 3"/>
    </svg>
    <div class="badge__text">
      <span class="badge__eyebrow">Neighbor Discount</span>
      <span class="badge__price">$9.95</span>
      <span class="badge__offer">Lawn fertilization<br>&amp; weed control</span>
      <span class="badge__note">First Service</span>
    </div>
  </div>

  <div class="brand">Fairlawn</div>
  <div class="brand__rule"></div>
  <div class="service-icons">
    <div class="service-icons__tile tile--grass" role="img" aria-label="Grass icon"></div>
    <div class="service-icons__tile tile--pest" role="img" aria-label="Insect icon"></div>
    <div class="service-icons__tile tile--soil" role="img" aria-label="Shovel in soil icon"></div>
  </div>

  <div class="headline">Lawn fertilization and weed control</div>
  <div class="write-in"></div>
  <div class="write-in__label">Representative</div>

  <ul class="service-list service-list--a">
    <li><span class="service-list__icon"></span>Lawn fertilization &amp; weed control</li>
    <li><span class="service-list__icon"></span>Sprinkler repair &amp; installation</li>
    <li><span class="service-list__icon"></span>Timer &amp; valve wiring</li>
    <li><span class="service-list__icon"></span>Xeriscape/drip conversion</li>
    <li><span class="service-list__icon"></span>Landscape design &amp; install</li>
    <li><span class="service-list__icon"></span>Pavers</li>
  </ul>
  <ul class="service-list service-list--b">
    <li><span class="service-list__icon"></span>Pergolas/pavillions</li>
    <li><span class="service-list__icon"></span>Retaining walls</li>
    <li><span class="service-list__icon"></span>Steel retaining</li>
    <li><span class="service-list__icon"></span>Water features</li>
    <li><span class="service-list__icon"></span>Landscape lighting</li>
    <li><span class="service-list__icon"></span>Fire features</li>
  </ul>

  <div class="tagline">Locally owned lawn &amp; pest control since 1990</div>
  <div class="cta">
    <span>FREE ESTIMATE</span>
    <span class="cta__phone">
      <svg viewBox="0 0 24 24" aria-hidden="true"><circle cx="12" cy="12" r="10" fill="none" stroke="#fff" stroke-width="2"/><path d="M8.5 7 L10.5 7 L11 9.5 L9.8 10.5 C10.5 12 12 13.5 13.5 14.2 L14.5 13 L17 13.5 L17 15.5 C17 16.3 16.3 17 15.5 17 C11 16.6 7.4 13 7 8.5 C7 7.7 7.7 7 8.5 7 Z" fill="#fff"/></svg>
      801-555-0147
    </span>
  </div>
  <div class="website">www.getfairlawn.com</div>
</section>

</body>
</html>
```